Fundraiser Flyer and Email Template

We are looking for a flexible coordinated flyer and email template. The feel of both should be more formal or professional. We are not looking for an overly "political" design that features American flags or other "political" symbols.

We are a political fundraising firm that works with elected officials to set up fundraisers for their campaigns. We send the invites to these events via US Mail and email, so we are looking for a standardized template that will work as both an 8.5 x 11 inch printed flyer, as well as an email template.

The information in the email will be text, but images can be used for formatting.

Some clients have a campaign logo, others do not. The format should be flexible enough to either include the logo, or leave it out. Size also varies.

Any colors in the template should be editable so we can match logos as we get them.

We're open to any format that allows us to edit the format as needed. This would include Photoshop, Microsoft Word, etc.

The text of the invite should include space for:

---------------------------------------
NAME
DISTRICT NUMBER AND OFFICE

DATE OF EVENT
TIME OF EVENT

LOCATION
LOCATION ADDRESS
LOCATION CITY, STATE, ZIP

SUGGESTED CONTRIBUTION LEVELS (Typically 3 levels are provided such as Gold: $1,000, Silver: $500, Bronze: $250)

ADDRESS TO SEND CHECKS TO

RSVP CONTACT INFORMATION

The invite will also need fine-print at the bottom that reads:
"Pennsylvania law allows personal, partnership, and PAC contributions. By law we cannot accept corporate contributions
Paid for by [NAME]"

It Professional

Serif
Sans Serif

• Must have spaces for:
• NAME
• DISTRICT NUMBER AND OFFICE
• DATE OF EVENT
• TIME OF EVENT
• LOCATION
• LOCATION ADDRESS
• LOCATION CITY, STATE, ZIP
• SUGGESTED CONTRIBUTION LEVELS (Typically 3 levels are provided such as Gold: $1,000, Silver: $500, Bronze: $250)
• ADDRESS TO SEND CHECKS TO
• RSVP CONTACT INFORMATION
• The invite will also need fine-print at the bottom that reads:
• "Pennsylvania law allows personal, partnership, and PAC contributions. By law we cannot accept corporate contributions
• Paid for by [NAME]"
• It should not be overly "political".

```html
<!DOCTYPE html>
<html lang="en">
<head>
<meta charset="utf-8">
<title>Fundraiser Invitation Template</title>
<link rel="stylesheet" href="https://fonts.googleapis.com/css2?family=Arimo:wght@400;700&display=swap">
<style>
  :root {
    --sky: #2aa9e1;
    --steel: #35769a;
    --mist: #aed5ef;
    --ink: #111111;
    --paper: #ffffff;
  }
  * { margin: 0; padding: 0; box-sizing: border-box; }
  html, body { width: 849px; height: 1200px; overflow: hidden; background: var(--paper); }
  .flyer {
    position: relative;
    width: 849px;
    height: 1200px;
    overflow: hidden;
    background: var(--paper);
    font-family: "Arimo", Helvetica, Arial, sans-serif;
    color: var(--ink);
  }
  .flyer__waves { position: absolute; inset: 0; width: 849px; height: 1200px; }
  .host {
    position: absolute;
    left: 34px;
    top: 131px;
    font-size: 32px;
    line-height: 41px;
    font-weight: 400;
  }
  .details {
    position: absolute;
    left: 189px;
    width: 500px;
    text-align: center;
    font-weight: 700;
  }
  .details--when { top: 278px; font-size: 32px; line-height: 41px; }
  .details--where { top: 384px; font-size: 32px; line-height: 41.3px; }
  .details--levels { top: 612px; font-size: 23px; line-height: 30.5px; }
  .details--levels .levels__title { font-size: 24px; margin-bottom: 8px; }
  .details--contact { top: 785px; font-size: 23px; line-height: 31px; }
  .logo-slot {
    position: absolute;
    left: 376px;
    top: 892px;
    width: 280px;
    height: 280px;
    display: flex;
    align-items: center;
    justify-content: center;
    font-size: 42px;
    font-weight: 700;
    color: var(--ink);
  }
  .fine-print {
    position: absolute;
    left: 6px;
    top: 1091px;
    width: 310px;
    font-size: 16px;
    line-height: 20.5px;
    font-weight: 700;
    color: var(--paper);
  }
</style>
</head>
<body>
<div class="flyer">
  <svg class="flyer__waves" viewBox="0 0 1061 1500" preserveAspectRatio="none" aria-hidden="true">
    <path d="M100 0 C500 40 850 200 1061 480 L1061 0 Z" fill="var(--steel)"/>
    <path d="M130 0 C520 30 880 180 1061 440 L1061 0 Z" fill="var(--mist)"/>
    <path d="M160 0 C560 20 900 150 1061 390 L1061 0 Z" fill="var(--sky)"/>
    <path d="M0 985 C100 1120 300 1280 490 1385 L490 1500 L0 1500 Z" fill="var(--steel)"/>
    <path d="M0 1050 C120 1190 300 1320 480 1402 L480 1500 L0 1500 Z" fill="var(--mist)"/>
    <path d="M0 1110 C150 1260 300 1350 470 1412 C620 1465 820 1480 1061 1500 L0 1500 Z" fill="var(--sky)"/>
    <circle cx="645" cy="1290" r="191" fill="var(--paper)" stroke="var(--sky)" stroke-width="23"/>
  </svg>

  <div class="host">
    <div class="host__name">NAME</div>
    <div class="host__office">DISTRICT NUMBER &amp; OFFICE</div>
  </div>

  <div class="details details--when">
    <div>DATE OF EVENT</div>
    <div>TIME OF EVENT</div>
  </div>

  <div class="details details--where">
    <div>LOCATION</div>
    <div>LOCATION ADDRESS</div>
    <div>LOCATION CITY,</div>
    <div>STATE</div>
    <div>ZIP</div>
  </div>

  <div class="details details--levels">
    <div class="levels__title">SUGGESTED CONTRIBUTION LEVELS</div>
    <div>Typically 3 levels are provided such as</div>
    <div>Gold: $1,000</div>
    <div>Silver: $500</div>
    <div>Bronze: $250</div>
  </div>

  <div class="details details--contact">
    <div>ADDRESS TO SEND CHECKS TO</div>
    <div>RSVP CONTACT INFORMATION</div>
  </div>

  <div class="logo-slot">LOGO</div>

  <p class="fine-print">"Pennsylvania law allows personal, partnership, and&nbsp; PAC contributions. By law we cannot accept corporate contributions<br>Paid for by [NAME]"</p>
</div>
</body>
</html>
```